Innovative Freezer Label Design

Create a versatile and innovative freezer label design with universal appeal, suitable for different functionalities. The design should cater to a diverse audience, including those who freeze meals for meal prepping, batch cooking, and the restaurant industry. Our vision is a visually striking and distinctive design that embodies simplicity.

Example "our current labels feature essential details like "Contents" and "Date." We recognize these as crucial points of information. Currently, the challenge lies in creating various labels for different marketplaces, considering language barriers. A proposed solution involves the integration of universal icons to replace specific words, promoting practicality for international sales."

Kindly note that design concepts should not be restricted to our current product, brand guideline, logo, or the provided example.

Our goal is not only product differentiation but also increased sales through a blend of functionality and aesthetics.

The following are examples of freezer labels designs. Kindly do not restrict your designs to the examples. The designs must be universal (for language barrier purposes)

Examples:
https://www.snaprovel.co.uk/pin/5820174630298837415/
https://www.snaprovel.co.uk/pin/5820174630298837419/
https://www.snaprovel.co.uk/pin/5820174630298837408/
https://www.snaprovel.co.uk/pin/5820174630298837322/
https://www.snaprovel.co.uk/pin/5820174630298898764/

Please reach out if you have any questions.

Thank you

```html
<!DOCTYPE html>
<html lang="en">
<head>
<meta charset="utf-8">
<title>Frostwell freezer labels</title>
<link href="https://fonts.googleapis.com/css2?family=EB+Garamond:wght@500&display=swap" rel="stylesheet">
<style>
  :root {
    --page: #f3f3f3;
    --paper: #ffffff;
    --brand: #34495a;
    --terracotta: #c0674b;
    --teal: #2d4f5a;
    --navy: #34495a;
    --sage: #9fb5aa;
  }
  * { box-sizing: border-box; margin: 0; padding: 0; }
  html, body { width: 1200px; height: 960px; overflow: hidden; }
  body {
    background: var(--page);
    position: relative;
    font-family: "EB Garamond", Georgia, serif;
  }
  .brand {
    position: absolute;
    left: 70px;
    top: 70px;
    font-size: 76px;
    font-weight: 500;
    color: var(--brand);
    letter-spacing: 1px;
  }
  .label {
    position: absolute;
    width: 387px;
    height: 226px;
    background: var(--paper);
    border-radius: 14px;
    box-shadow: 0 3px 10px rgba(0,0,0,0.10);
    color: var(--ink);
  }
  .label::before {
    content: "";
    position: absolute;
    inset: 7px;
    border: 1.3px solid var(--ink);
    border-radius: 13px;
  }
  .label--terracotta { --ink: var(--terracotta); left: 206px; top: 302px; }
  .label--teal { --ink: var(--teal); left: 622px; top: 302px; }
  .label--navy { --ink: var(--navy); left: 206px; top: 560px; }
  .label--sage { --ink: var(--sage); left: 622px; top: 560px; }

  .icon {
    position: absolute;
    fill: none;
    stroke: currentColor;
    stroke-width: 1.8;
    stroke-linecap: round;
    stroke-linejoin: round;
    filter: drop-shadow(2px 3px 3px rgba(0,0,0,0.14));
  }
  .icon--meal { left: 52px; top: 57px; width: 60px; height: 52px; }
  .icon--date { left: 58px; top: 129px; width: 52px; height: 52px; }

  .write-line {
    position: absolute;
    left: 129px;
    width: 193px;
    height: 0;
    border-top: 1.6px solid var(--ink);
  }
  .write-line--contents { top: 99px; }
  .write-line--date { top: 176px; }

  .date-slash {
    position: absolute;
    top: 140px;
    font-family: "EB Garamond", Georgia, serif;
    font-size: 28px;
    line-height: 1;
    color: var(--ink);
  }
  .date-slash--first { left: 195px; }
  .date-slash--second { left: 252px; }

  .label-brand {
    position: absolute;
    right: 22px;
    top: 22px;
    font-size: 17px;
    font-weight: 500;
    color: var(--ink);
  }
</style>
</head>
<body>
  <div class="brand">Frostwell</div>

  <!-- reusable icon definitions -->
  <svg width="0" height="0" style="position:absolute">
    <defs>
      <symbol id="meal" viewBox="0 0 60 52">
        <path d="M3 3v11a4.5 4.5 0 0 0 9 0V3M7.5 3v11M7.5 19v30"/>
        <circle cx="31" cy="26" r="19"/>
        <circle cx="31" cy="26" r="13"/>
        <path d="M54 49V3c3.5 2 5 11 5 21h-5"/>
      </symbol>
      <symbol id="date" viewBox="0 0 52 52">
        <rect x="2" y="8" width="48" height="42" rx="5"/>
        <path d="M2 18h48M12 5h30"/>
        <circle cx="12" cy="5" r="3"/>
        <circle cx="22" cy="5" r="3"/>
        <circle cx="32" cy="5" r="3"/>
        <circle cx="42" cy="5" r="3"/>
        <rect x="10" y="24" width="7" height="7" rx="1.5"/>
        <rect x="23" y="24" width="7" height="7" rx="1.5"/>
        <rect x="36" y="24" width="7" height="7" rx="1.5"/>
        <rect x="10" y="37" width="7" height="7" rx="1.5"/>
        <rect x="23" y="37" width="7" height="7" rx="1.5"/>
        <path d="M43 37h-5.5a1.5 1.5 0 0 0-1.5 1.5v4a1.5 1.5 0 0 0 1.5 1.5H43"/>
      </symbol>
    </defs>
  </svg>

  <div class="label label--terracotta">
    <svg class="icon icon--meal"><use href="#meal"/></svg>
    <svg class="icon icon--date"><use href="#date"/></svg>
    <span class="date-slash date-slash--first">/</span>
    <span class="date-slash date-slash--second">/</span>
  </div>

  <div class="label label--teal">
    <svg class="icon icon--meal"><use href="#meal"/></svg>
    <svg class="icon icon--date"><use href="#date"/></svg>
    <div class="write-line write-line--contents"></div>
    <div class="write-line write-line--date"></div>
    <span class="date-slash date-slash--first">/</span>
    <span class="date-slash date-slash--second">/</span>
  </div>

  <div class="label label--navy">
    <span class="label-brand">Frostwell</span>
    <svg class="icon icon--meal"><use href="#meal"/></svg>
    <svg class="icon icon--date"><use href="#date"/></svg>
    <div class="write-line write-line--contents"></div>
    <div class="write-line write-line--date"></div>
    <span class="date-slash date-slash--first">/</span>
    <span class="date-slash date-slash--second">/</span>
  </div>

  <div class="label label--sage">
    <span class="label-brand">Frostwell</span>
    <svg class="icon icon--meal"><use href="#meal"/></svg>
    <svg class="icon icon--date"><use href="#date"/></svg>
    <span class="date-slash date-slash--first">/</span>
    <span class="date-slash date-slash--second">/</span>
  </div>
</body>
</html>
```